Lueur de Provins Immerse in the enchanting flavors of France at Lueur de Provins

A menu that is French in style with the Eiffel Tower. A elegant menu that is in rich blue with red or gold trimmings, we are a French Bakey and Cafe

Target Market(s)

30 to 55 people

Industry/Entity Type

Restaurant

Font styles to use
Decorative

Colors
0054AA
0677BA
7BADD7
CADEEF
E8F1F8
EB3D1F
EC4F4E
F09395
F8D3D4
FCEDEE

Requirements
Must have
• the attachment "My Brunch Specials" is the Menu I want you to create, it has all the text, "My Brunch Special Complete" is a word version. The menu size should be 4 1/4 wide by 14 inches long 2 Sided. must have our logo at the top , Make the font larger, because our biggest complaint about our menu is it is hard to read
Nice to have
• I would love to incorporate the Eiffel Tower as a silhouette in the background
Should not have
• I do not want too many pictures or small print

```html
<!DOCTYPE html>
<html lang="en">
<head>
<meta charset="utf-8">
<title>Lueur de Provins – Brunch &amp; Drink Specials</title>
<link rel="stylesheet" href="https://fonts.googleapis.com/css2?family=Yanone+Kaffeesatz:wght@500&family=Kalam:wght@700&family=Open+Sans:wght@400&family=Josefin+Sans:wght@400&display=swap">
<style>
  :root {
    --backdrop: #9a9a9a;
    --paper: #ffffff;
    --navy: #1f2d5a;
    --red: #c4382f;
    --maroon: #5a1e2c;
    --cream: #fbf3ea;
    --ink: #1a1a1a;
    --card-line: #c8c8c8;
  }
  * { box-sizing: border-box; margin: 0; padding: 0; }
  html, body { width: 1200px; height: 1200px; overflow: hidden; }
  body { background: var(--backdrop); position: relative; font-family: "Open Sans", sans-serif; color: var(--ink); }

  .menu-side { position: absolute; top: 62px; width: 326px; height: 1076px; background: var(--paper); overflow: hidden; }
  .menu-side--food { left: 247px; }
  .menu-side--drinks { left: 627px; }

  .header-frame { position: absolute; left: 10px; top: 14px; width: 305px; height: 140px; border: 1px solid var(--red); border-bottom: none; }
  .header-ornament { position: absolute; left: 67px; top: 9px; width: 193px; height: 24px; background: linear-gradient(90deg, #c9a6ad, var(--maroon), #c9a6ad); border-radius: 12px; opacity: .8; }
  .brand-mark { position: absolute; left: 145px; top: 58px; width: 36px; height: 36px; background: var(--navy); }
  .brand-name { position: absolute; left: 0; right: 0; top: 110px; text-align: center; font-family: "Josefin Sans", sans-serif; font-size: 13px; letter-spacing: 6px; color: var(--navy); text-transform: uppercase; }

  .section-title { position: absolute; left: 0; right: 0; text-align: center; font-family: "Kalam", cursive; font-weight: 700; color: var(--red); line-height: 1; }
  .section-title--brunch { top: 138px; font-size: 35px; }
  .section-title--drinks { top: 12px; font-size: 35px; }
  .section-title--latte { top: 622px; font-size: 33px; }

  .tower-silhouette { position: absolute; top: 782px; width: 98px; height: 294px; background: linear-gradient(180deg, var(--navy) 0%, #8a3a4e 45%, var(--red) 100%); opacity: .85; clip-path: polygon(46% 0, 54% 0, 62% 40%, 100% 100%, 0 100%, 38% 40%); z-index: 0; }
  .menu-side--food .tower-silhouette { left: 228px; }
  .menu-side--drinks .tower-silhouette { left: 0; width: 106px; }

  .menu-item { position: absolute; left: 14px; width: 298px; z-index: 1; }
  .menu-item--narrow { width: 255px; }
  .menu-item--latte { left: 57px; width: 255px; }

  .menu-item__body { position: absolute; top: 13px; left: 0; right: 0; bottom: 0; background: var(--paper); border: 1px solid var(--card-line); border-radius: 6px; padding: 15px 10px 3px; font-size: 8.2px; line-height: 11.3px; text-align: justify; text-align-last: center; display: flex; align-items: center; }

  .ribbon { position: absolute; top: 0; left: 50%; transform: translateX(-50%); display: flex; height: 26px; background: var(--maroon); padding: 2px 10px 2px 14px; clip-path: polygon(0 0, 100% 0, 94% 50%, 100% 100%, 0 100%, 6% 50%); white-space: nowrap; z-index: 2; }
  .ribbon__name { background: var(--cream); color: var(--navy); font-family: "Yanone Kaffeesatz", sans-serif; font-weight: 500; font-size: 19px; line-height: 22px; padding: 0 6px 0 10px; }
  .ribbon__price { background: var(--red); color: #fff; font-family: "Yanone Kaffeesatz", sans-serif; font-weight: 500; font-size: 19px; line-height: 22px; padding: 0 10px 0 7px; border-radius: 11px 0 0 11px; }
</style>
</head>
<body>

<section class="menu-side menu-side--food">
  <div class="header-frame"></div>
  <div class="header-ornament" role="img" aria-label="Decorative scrollwork flourish"></div>
  <div class="brand-mark"></div>
  <div class="brand-name">Lueur de Provins</div>
  <h1 class="section-title section-title--brunch">Brunch Specials</h1>

  <div class="tower-silhouette" role="img" aria-label="Eiffel Tower illustration in navy and red"></div>

  <article class="menu-item" style="top:190px;height:101px">
    <h2 class="ribbon"><span class="ribbon__name">Beef Bourguignon -</span><span class="ribbon__price">$18</span></h2>
    <p class="menu-item__body">Indulge in our rich and comforting flavors of savory, tender beef slowly braised in red wine, creating a luscious sauce that envelops pearl onions, carrots, and mushrooms in a symphony of flavors. Served alongside buttered egg noodles. It’s a hearty and soul-warming meal that promises pure culinary bliss.</p>
  </article>

  <article class="menu-item" style="top:296px;height:123px">
    <h2 class="ribbon"><span class="ribbon__name">Ratatouille and eggs -</span><span class="ribbon__price">$18</span></h2>
    <p class="menu-item__body">Experience the essence of Provence with our Ratatouille, a vibrant medley of roasted squash, peppers, tomatoes, eggplant, infused with fragrant fresh herbs. Served with two perfectly poached eggs, and your choice of flavorful andouille sausage or crispy bacon. Accompanied by a side of crusty baguette. It’s a hearty dish that celebrates the flavors of the Mediterranean countryside.</p>
  </article>

  <article class="menu-item" style="top:426px;height:113px">
    <h2 class="ribbon"><span class="ribbon__name">Tourte au Poulet -</span><span class="ribbon__price">$15</span></h2>
    <p class="menu-item__body">Ratatouille and eggsDiscover the indulgent flavors of our Tourte au Poulet, a savory delight that marries tender marinated chicken with the richness of Swiss cheese and the sweetness of onions, all encased in layers of flaky pastry. Topped with a savory mushroom medley and decadent bechamel sauce. A true comfort classic to delight your senses.</p>
  </article>

  <article class="menu-item" style="top:545px;height:136px">
    <h2 class="ribbon"><span class="ribbon__name">Le Grande Breakfast -</span><span class="ribbon__price">$15</span></h2>
    <p class="menu-item__body">Start your day in style with our Le Grande Breakfast, a feast fit for royalty. Customize your morning indulgence with two eggs cooked to your preference, paired with either savory bacon or succulent chicken sausage. Choose between a freshly baked baguette or a buttery croissant to accompany your meal. Complete your breakfast by selecting from an array of sides including crispy hash browns, savory roasted potatoes, or a refreshing fruit salad. Bon appetit!</p>
  </article>

  <article class="menu-item" style="top:691px;height:127px">
    <h2 class="ribbon"><span class="ribbon__name">Smoked Salmon Tartine -</span><span class="ribbon__price">$14</span></h2>
    <p class="menu-item__body">Delight in the luxurious flavors of our Smoked Salmon Tartine, a culinary, masterpiece that elevates breakfast to new heights. Indulge in truffled scrambled eggs nestled atop smoked salmon, adorned with tangy pickled red onions, briny caper berries, crisp cucumber, juicy tomato, and peppery arugula. All artfully arranged on multigrain bread generously spread with herb-infused cream cheese.</p>
  </article>

  <article class="menu-item menu-item--narrow" style="top:827px;height:111px">
    <h2 class="ribbon"><span class="ribbon__name">Le Benedict Salmon -</span><span class="ribbon__price">$14</span></h2>
    <p class="menu-item__body">Savor the classic elegance of Eggs Benedict, featuring two perfectly poached eggs nestled on toasted English muffins, with luscious smoked salmon and ripe tomato slices crowned with a velvety lemon-infused Hollandaise sauce. A timeless brunch delight crafted to perfection.</p>
  </article>

  <article class="menu-item menu-item--narrow" style="top:945px;height:103px">
    <h2 class="ribbon"><span class="ribbon__name">Salmon Atlantique -</span><span class="ribbon__price">$14</span></h2>
    <p class="menu-item__body">Enjoy a bed of crisp mixed greens adorned with delicate smoked salmon, sweet golden raisins, creamy goat cheese, and crunchy walnuts. All dressed in a tantalizing balsamic vinaigrette that ties the elements together perfectly.</p>
  </article>
</section>

<section class="menu-side menu-side--drinks">
  <h1 class="section-title section-title--drinks">Drink Specials</h1>

  <div class="tower-silhouette" role="img" aria-label="Eiffel Tower illustration in navy and red"></div>

  <article class="menu-item" style="top:60px;height:112px">
    <h2 class="ribbon"><span class="ribbon__name">Bottomless Mimosa -</span><span class="ribbon__price">$18</span></h2>
    <p class="menu-item__body">Embark on an endless journey of delight with our Bottomless Mimosa, featuring Marlowe champagne, infusing each sip with a sparkling sensation. Tailor your experience with your preferred flavor profile - opt for the timeless twist of classic orange juice or tangy cranberry juice for a refreshing zing. Continuously poured to ensure your glass is always full.</p>
  </article>

  <article class="menu-item" style="top:176px;height:112px">
    <h2 class="ribbon"><span class="ribbon__name">Blood Orange/Pineapple Spritz -</span><span class="ribbon__price">$12</span></h2>
    <p class="menu-item__body">Introducing our vibrant spritz cocktail, a tantalizing blend of Fenwick &amp; Hale's premium Verenka Vodka, sweet vermouth, and a touch of sweetness from a carefully muddled sugar cube. This effervescent libation reaches new heights with the addition of bubbly Clairsource, your choice of either Blood Orange or Pineapple syrup injects a burst of fruity allure into every sip.</p>
  </article>

  <article class="menu-item" style="top:292px;height:78px">
    <h2 class="ribbon"><span class="ribbon__name">Espresso Martini -</span><span class="ribbon__price">$10</span></h2>
    <p class="menu-item__body">Our Espresso Martini is a decadent blend of bold espresso, rich chocolate martini, and luxurious Bellarosa chocolate syrup. It's the ultimate indulgence for coffee and chocolate lovers a like.</p>
  </article>

  <article class="menu-item" style="top:374px;height:78px">
    <h2 class="ribbon"><span class="ribbon__name">Kir Royale -</span><span class="ribbon__price">$10</span></h2>
    <p class="menu-item__body">Our Kir Royale is a delightful fusion of the crisp, sparkling champagne bubbles and the sweet sophistication of black currant. a luxurious and indulgent drink that's perfect for any occasion.</p>
  </article>

  <article class="menu-item" style="top:456px;height:80px">
    <h2 class="ribbon"><span class="ribbon__name">Apple Cider-Mimosa -</span><span class="ribbon__price">$9</span></h2>
    <p class="menu-item__body">A delightful twist on the classic mimosa. Crafted with champagne and crisp apple cider. To elevate the experience, we adorn the glass with a caramel rim dipped in brown sugar, adding a touch of indulgent sweetness to every sip.</p>
  </article>

  <article class="menu-item" style="top:540px;height:78px">
    <h2 class="ribbon"><span class="ribbon__name">Peach Bellini -</span><span class="ribbon__price">$9</span></h2>
    <p class="menu-item__body">Try our perfectly balanced Peach Bellini with each sip you capture the crispness of champagne with the irresistible sweetness of peach. It's a sublime fusion of sophistication and sweetness.</p>
  </article>

  <h1 class="section-title section-title--latte">Latte</h1>

  <article class="menu-item menu-item--latte" style="top:662px;height:125px">
    <h2 class="ribbon"><span class="ribbon__name">Truffle Latte -</span><span class="ribbon__price">$14</span></h2>
    <p class="menu-item__body">We start with rich Bellarosa chocolate, known for its velvety smoothness and intense flavor. Then, we add a drizzle of salted caramel, adding a perfect balance of sweetness and a hint of savory richness. Finally, we combine this delightful blend with perfectly steamed milk to create a creamy and indulgent latte that will satisfy even the most discerning palate.</p>
  </article>

  <article class="menu-item menu-item--latte" style="top:791px;height:113px">
    <h2 class="ribbon"><span class="ribbon__name">Napoleon Latte -</span><span class="ribbon__price">$6</span></h2>
    <p class="menu-item__body">We start with our rich espresso, renowned for its bold and robust character. Then, we add a luscious combination of hazelnut and vanilla syrup, creating a symphony of sweetness and nutty richness. As the final touch, we crown this masterpiece with the velvety smoothness of perfectly steamed milk.</p>
  </article>

  <article class="menu-item menu-item--latte" style="top:908px;height:128px">
    <h2 class="ribbon"><span class="ribbon__name">Chai Latte -</span><span class="ribbon__price">$6</span></h2>
    <p class="menu-item__body">Our robust chai tea concentrate, infused with a symphony of cinnamon, cardamom, cloves, and ginger, sets the stage for a journey of aromatic delight. Paired with velvety steamed milk, each sip offers a harmonious blend of bold spices and creamy richness. Topped with a sprinkle of cinnamon, it's the perfect finishing touch to this comforting treat.</p>
  </article>
</section>

</body>
</html>
```